UK Based Internet hosting Company wants a vibrant eCommerce site designed.

We have only just had our logo and brand designed by Pixel Forum which went so well that we would like to open up our website design project on here too.

The company is called 'Quay Server Lantern' and we provide a range of website hosting, dedicated server, domain name and email solutions that people will be able to purchase online in neatly packaged options from the outset.

Our logo and brand is bright turquoise, black & white (samples of branding will be attached with this project) but we would like the website to be very vibrant with good use of white space rather than a black website.

We want to appeal to end users so web designers, developers and people who would like to host their website. But we also want to appeal to resellers that would like to resell our hosting packages too.

We want a big push on social media and blogging on the site as we would like our brand to be 100% up with Chatterleaf, Murmel, workLoop, Vidplume and Zorbix+. It would be great to have this integrated into the site with share buttons and rating buttons etc.

We would like to see a homepage initially with a view to providing several page layers down to help our in-house developers hook in our back-end into this front end effectively.

Great customer experience and an easy to navigate journey to the checkout when purchasing the hosting packages is paramount !!

We like how the following sites are set-out and presented:

www.brightmarrow.uk
http://www.tallyfold.co.uk
https://www.qv7.net/web-hosting/

Target Market(s)

We have 3 target markets.

Target market 1 - end users, consumers such as Web Designers, Developers and small businesses.

Target Market 2 - Resellers, small businesses that would like to resell our services.

Target Market 3 - Medium to large businesses that would like more of a bespoke solution.

Industry/Entity Type

Internet

Requirements
Must have
• Colourful, bright, bold, easy to navigate and to purchase packages.
• Plenty of call to actions, social media, ratings.
• Video case studies and testimonials would be nice.

```html
<!DOCTYPE html>
<html lang="en">
<head>
<meta charset="utf-8">
<title>Quay Server Lantern – Web Hosting</title>
<link href="https://fonts.googleapis.com/css2?family=Raleway:wght@300;400;600;700;800&family=Open+Sans:wght@400;600;700&display=swap" rel="stylesheet">
<style>
:root{
  --teal:#21b8c1;
  --teal-dark:#1a9aa2;
  --mint:#2ee6b5;
  --ink:#1c1f26;
  --nav:#181c27;
  --bar:#303135;
  --text:#333;
  --muted:#777;
  --light:#f1f1f1;
  --footer:#1d1d1f;
  --white:#fff;
}
*{box-sizing:border-box;margin:0;padding:0}
html,body{width:1200px;height:3879px;overflow:hidden}
body{font-family:"Open Sans",Arial,sans-serif;color:var(--text);background:var(--white);font-size:14px;position:relative}
h1,h2,h3,h4{font-family:"Raleway",Arial,sans-serif}
section,header,footer{position:relative;width:1200px;overflow:hidden}
.abs{position:absolute}

/* header */
.site-header{height:104px;background:var(--nav)}
.brand{left:103px;top:24px;display:flex;align-items:center;gap:14px}
.brand-dot{width:56px;height:56px;border-radius:50%;background:var(--teal)}
.brand-name{font-family:"Raleway",sans-serif;font-weight:600;font-size:26px;color:var(--white)}
.login-btn{left:1034px;top:16px;width:66px;height:28px;background:var(--teal);color:#fff;font-size:13px;border-radius:3px;display:flex;align-items:center;justify-content:center}
.main-nav{right:100px;top:72px;display:flex;gap:38px;font-size:14px;color:#fff}

/* hero */
.hero{height:612px;background:linear-gradient(90deg,#ececec 0%,#dcdcdc 45%,#c7c7c7 100%)}
.hero-person{left:608px;top:0;width:478px;height:612px;background:linear-gradient(180deg,#b9b9b9 0%,#5a5f66 40%,#2a2d33 100%);border-radius:200px 200px 0 0}
.hero-copy{left:116px;top:150px}
.hero-title-light{font-weight:300;font-size:62px;letter-spacing:3px;color:var(--ink);line-height:1}
.hero-title-bold{font-weight:700;font-size:62px;letter-spacing:2px;color:var(--ink);line-height:1.15}
.hero-list{list-style:none;margin-top:30px}
.hero-list li{font-size:17px;color:#333;height:30px;display:flex;align-items:center;gap:12px}
.hero-list svg{width:14px;height:14px}
.btn-teal{background:var(--teal);color:#fff;border-radius:4px;display:inline-flex;align-items:center;justify-content:center}
.hero-cta{margin-top:26px;width:124px;height:40px;font-size:16px}

/* domain bar */
.domain-bar{height:101px;background:var(--bar);color:#fff}
.domain-bar .prices{left:101px;top:0;height:101px;display:flex;align-items:center;gap:26px;font-size:17px}
.prices .label{color:var(--teal);margin-right:14px}
.bar-search{left:693px;top:25px;width:407px;height:52px;border:4px solid #fff;display:flex}
.bar-search .field{flex:1;background:#fff;color:#999;font-size:14px;display:flex;align-items:center;padding-left:14px}
.bar-search .go{width:88px;background:var(--teal);font-size:15px;display:flex;align-items:center;justify-content:center}

/* section heads */
.sec-title{font-size:34px;font-weight:700;color:var(--ink);text-align:center;letter-spacing:1px}
.sec-title span{color:var(--teal)}
.sec-lead{width:730px;margin:18px auto 0;text-align:center;color:#666;font-size:14px;line-height:1.55}

/* welcome */
.welcome{height:559px}
.welcome .sec-title{padding-top:46px}
.price-cards{left:103px;top:192px;display:flex;gap:26px}
.price-card{width:314px;height:284px;border:1px solid #ddd;background:#fff;text-align:center;padding-top:54px;position:relative;box-shadow:0 2px 4px rgba(0,0,0,.08)}
.price-card .kicker{font-size:12px;letter-spacing:1px;color:#222}
.price-card .amount{font-family:"Raleway",sans-serif;font-weight:700;font-size:36px;color:#222;margin-top:4px}
.price-card h3{font-weight:400;font-size:25px;letter-spacing:1px;color:#222;margin-top:6px}
.price-card p{font-size:13px;line-height:1.5;width:220px;margin:10px auto 0;color:#222}
.price-card svg{position:absolute;left:-1px;bottom:-22px;width:314px;height:22px}
.price-card.featured{background:var(--teal);border-color:var(--teal)}
.price-card.featured *{color:#fff}

/* domain search */
.domain-search{height:442px;background:linear-gradient(135deg,#3a4047 0%,#23272c 50%,#30363c 100%)}
.domain-search h2{left:171px;top:92px;color:#fff;font-size:34px;font-weight:700;letter-spacing:1px}
.ds-form{left:171px;top:170px;width:721px;height:86px;background:#fff;border:4px solid #2c2f33;display:flex}
.ds-form .field{flex:1;color:#999;font-size:15px;display:flex;align-items:center;padding-left:22px}
.ds-form .tld{width:96px;background:#2c2f33;color:#fff;font-size:15px;display:flex;align-items:center;justify-content:center;gap:10px}
.ds-btn{left:910px;top:170px;width:171px;height:86px;font-size:14px;border-radius:0}
.ds-step{top:326px;display:flex;align-items:center;gap:18px;color:#fff;font-size:15px}
.ds-step b{width:38px;height:38px;border-radius:50%;background:var(--teal);display:flex;align-items:center;justify-content:center;font-weight:600}

/* plans */
.plans{height:597px}
.plans .sec-title{padding-top:32px}
.plan-grid{left:103px;top:163px;display:flex;gap:15px}
.plan{width:238px}
.plan-tab{height:36px;background:var(--mint);color:#fff;font-family:"Raleway",sans-serif;font-weight:700;font-size:22px;text-align:center;line-height:36px;position:relative}
.plan-tab::after{content:"";position:absolute;left:50%;bottom:-10px;margin-left:-10px;border:10px solid transparent;border-bottom:0;border-top-color:var(--mint)}
.plan-body{margin-top:10px;height:326px;background:var(--teal);color:#fff;text-align:center;padding-top:24px}
.plan-body .rate{font-size:24px;margin-bottom:8px}
.plan-body li{list-style:none;font-size:15px;height:40px;line-height:40px}
.plan-body .signup{display:inline-block;margin-top:6px;background:#fff;color:var(--teal);width:116px;height:38px;line-height:38px;border-radius:3px;font-size:17px}

/* hot / why */
.hot-why{height:443px;background:linear-gradient(90deg,#eeeeee 0%,#e4e4e4 60%,#d8d8d8 100%)}
.col-title{font-size:34px;font-weight:600;color:var(--ink);letter-spacing:1px}
.col-rule{width:100px;height:3px;background:var(--teal);margin-top:14px}
.hot-col{left:103px;top:40px}
.why-col{left:618px;top:40px}
.hot-banner{left:103px;top:140px;width:481px;height:243px;background:#1d1d1d}
.hot-banner .server{left:30px;top:20px;width:100px;height:200px;background:linear-gradient(180deg,#555,#111)}
.hot-banner .text{left:178px;top:52px;color:#fff}
.hot-banner .small{font-size:18px}
.hot-banner .big{font-family:"Raleway",sans-serif;font-weight:700;font-size:44px;line-height:1;letter-spacing:1px}
.hot-banner .big em{font-style:normal;color:var(--teal)}
.hot-banner .more{margin-top:18px;width:76px;height:26px;font-size:11px;border-radius:2px}
.hot-banner .badge{left:80px;top:150px;width:60px;height:60px;border-radius:50%;background:#f6b90b}
.dots{display:flex;gap:8px}
.dots i{width:8px;height:8px;border-radius:50%;background:#888}
.dots i.on{background:var(--teal)}
.why-item{left:626px;display:flex;gap:24px;width:474px}
.why-item .photo{width:93px;height:93px;border-radius:50%;background:linear-gradient(180deg,#c8c8c8,#6d6d6d);flex:none}
.why-item h4{font-size:14px;font-weight:700;color:#222;margin-top:4px}
.why-item p{font-size:13px;line-height:1.5;color:#666;margin-top:6px}

/* testimonials */
.voices{height:413px}
.voices .col-title{font-size:34px}
.voices .col-title b{font-weight:800}
.quote-box{left:106px;top:142px;width:478px;height:116px;border:1px solid #ddd;padding:16px 20px;font-size:13px;line-height:1.55;color:#444}
.quote-box::after{content:"";position:absolute;left:30px;bottom:-10px;width:18px;height:18px;background:#fff;border-right:1px solid #ddd;border-bottom:1px solid #ddd;transform:rotate(45deg)}
.author{left:106px;top:271px;display:flex;gap:16px;align-items:center}
.author .avatar{width:65px;height:65px;background:linear-gradient(180deg,#8a7a6c,#333)}
.author .name{font-size:14px;color:#222}
.author .role{font-size:12px;color:#555;margin-top:6px}
.author .role span{color:var(--teal)}
.site-list{left:628px;top:142px}
.site-list h4{font-family:"Open Sans",sans-serif;font-size:14px;font-weight:600;color:#222;margin-bottom:10px}
.site-list li{list-style:none;font-size:13px;color:#444;height:24px;display:flex;align-items:center;gap:10px}
.site-list svg{width:12px;height:12px}
.monitor{left:905px;top:142px;width:195px;height:150px;background:linear-gradient(180deg,#e7eef4,#9fb3c4);border:8px solid #222;border-radius:4px}
.monitor-stand{left:975px;top:292px;width:60px;height:40px;background:#ccc;clip-path:polygon(30% 0,70% 0,100% 100%,0 100%)}
.start-badge{left:880px;top:128px;width:70px;height:70px;border-radius:50%;background:#f6b90b;color:#222;font-size:12px;text-align:center;line-height:1.2;padding-top:16px}

/* contact strip */
.contact-strip{height:99px;background:var(--mint);color:#fff}
.contact-item{top:18px;width:200px;margin-left:-100px;text-align:center;font-size:17px}
.contact-item svg{width:28px;height:28px;display:block;margin:0 auto 8px}

/* footer */
.site-footer{height:406px;background:var(--footer);color:#9a9a9a}
.foot-col{top:62px;width:230px}
.foot-col h4{color:#fff;font-size:17px;font-weight:600;padding-bottom:14px;border-bottom:1px solid #3a3a3a}
.foot-col ul{list-style:none;margin-top:20px}
.foot-col li{font-size:12px;height:24px;line-height:24px}
.news-label{font-size:12px;margin-top:4px}
.news-form{display:flex;margin-top:10px;width:226px;height:34px}
.news-form .field{flex:1;background:#fff;color:#999;font-size:11px;display:flex;align-items:center;padding-left:8px}
.news-form .go{width:60px;background:var(--teal);color:#fff;font-size:12px;display:flex;align-items:center;justify-content:center}
.post{display:flex;gap:14px;margin-top:20px}
.post .thumb{width:54px;height:50px;background:linear-gradient(135deg,#d9d9d9,#777);flex:none}
.post .t{color:var(--teal);font-size:12px;font-weight:600}
.post .d{font-size:12px;margin-top:2px}
.post .m{font-size:10px;margin-top:2px;color:#777}

/* copyright */
.copy-bar{height:103px;background:var(--teal);color:#fff}
.copy-bar p{left:160px;top:0;line-height:103px;font-size:15px}
.socials{left:853px;top:36px;display:flex;gap:14px}
.socials span{width:30px;height:30px;border-radius:50%;border:2px solid rgba(255,255,255,.8)}
</style>
</head>
<body>

<header class="site-header">
  <div class="brand abs"><span class="brand-dot"></span><span class="brand-name">Quay Server Lantern</span></div>
  <div class="login-btn abs">Login</div>
  <nav class="main-nav abs"><span>Home</span><span>Layouts</span><span>Domains</span><span>Hosting</span><span>Elements</span><span>Pages</span><span>Portfolio</span><span>Contact</span></nav>
</header>

<section class="hero" role="img" aria-label="Office background photo with a smiling businessman in a suit">
  <div class="hero-person abs" role="img" aria-label="Businessman in dark suit and glasses"></div>
  <div class="hero-copy abs">
    <h1 class="hero-title-light">UNLIMITED</h1>
    <h1 class="hero-title-bold">WEB HOSTING</h1>
    <ul class="hero-list">
      <li><svg viewBox="0 0 14 14"><rect x="1" y="1" width="12" height="12" fill="none" stroke="#333" stroke-width="1.5"/><path d="M3.5 7l2.5 2.5 5-6" fill="none" stroke="#333" stroke-width="1.6"/></svg>Unlimited Disk Space, Bandwidth &amp; Email Addresses</li>
      <li><svg viewBox="0 0 14 14"><rect x="1" y="1" width="12" height="12" fill="none" stroke="#333" stroke-width="1.5"/><path d="M3.5 7l2.5 2.5 5-6" fill="none" stroke="#333" stroke-width="1.6"/></svg>FREE Domain Registration</li>
      <li><svg viewBox="0 0 14 14"><rect x="1" y="1" width="12" height="12" fill="none" stroke="#333" stroke-width="1.5"/><path d="M3.5 7l2.5 2.5 5-6" fill="none" stroke="#333" stroke-width="1.6"/></svg>FREE Security Suite</li>
      <li><svg viewBox="0 0 14 14"><rect x="1" y="1" width="12" height="12" fill="none" stroke="#333" stroke-width="1.5"/><path d="M3.5 7l2.5 2.5 5-6" fill="none" stroke="#333" stroke-width="1.6"/></svg>FREE Site-Building Tools</li>
      <li><svg viewBox="0 0 14 14"><rect x="1" y="1" width="12" height="12" fill="none" stroke="#333" stroke-width="1.5"/><path d="M3.5 7l2.5 2.5 5-6" fill="none" stroke="#333" stroke-width="1.6"/></svg>FREE Search Engine &amp; Marketing Credits</li>
      <li><svg viewBox="0 0 14 14"><rect x="1" y="1" width="12" height="12" fill="none" stroke="#333" stroke-width="1.5"/><path d="M3.5 7l2.5 2.5 5-6" fill="none" stroke="#333" stroke-width="1.6"/></svg>FREE Security Suite</li>
    </ul>
    <span class="btn-teal hero-cta">Get Started</span>
  </div>
</section>

<section class="domain-bar">
  <div class="prices abs"><span class="label">Top Domains</span><span>.com $11.99</span><span>|</span><span>.org $11.99</span><span>|</span><span>.net $10.99</span></div>
  <div class="bar-search abs"><span class="field">Enter Your Domain Name Here</span><span class="go">Search</span></div>
</section>

<section class="welcome">
  <h2 class="sec-title">WELCOME TO <span>QUAY SERVER LANTERN</span></h2>
  <p class="sec-lead">Lorem ipsum dolor sit amet, consectetuer adipiscing elit. Suspendisse et justo. Praesent mattis commodo augue. Aliquam ornare hendrerit augue.</p>
  <div class="price-cards abs">
    <div class="price-card"><div class="kicker">STARTING AT</div><div class="amount">$ 16.99</div><h3>RESELLER HOSTING</h3><p>Lorem Ipsum has been the industry's standard dummy text ever</p><svg viewBox="0 0 314 22" preserveAspectRatio="none"><polygon points="0,0 314,0 314,22 200,8" fill="#21b8c1"/></svg></div>
    <div class="price-card featured"><div class="kicker">STARTING AT</div><div class="amount">$ 16.99</div><h3>VPS HOSTING</h3><p>Lorem Ipsum has been the industry's standard dummy text ever</p><svg viewBox="0 0 314 22" preserveAspectRatio="none"><polygon points="0,0 314,0 314,22 200,8" fill="#1a9aa2"/></svg></div>
    <div class="price-card"><div class="kicker">STARTING AT</div><div class="amount">$ 16.99</div><h3>DEDICATED SERVERS</h3><p>Lorem Ipsum has been the industry's standard dummy text ever</p><svg viewBox="0 0 314 22" preserveAspectRatio="none"><polygon points="0,0 314,0 314,22 200,8" fill="#21b8c1"/></svg></div>
  </div>
</section>

<section class="domain-search" role="img" aria-label="Dim photo of server racks in a data centre">
  <h2 class="abs">DOMAIN SEARCH</h2>
  <div class="ds-form abs"><span class="field">Enter Your Domain Name Here</span><span class="tld">.COM <svg width="10" height="6" viewBox="0 0 10 6"><path d="M0 0h10L5 6z" fill="#fff"/></svg></span></div>
  <span class="btn-teal ds-btn abs">SEARCH DOMAIN</span>
  <div class="ds-step abs" style="left:170px"><b>1</b>WRITE A DOMAIN NAME</div>
  <div class="ds-step abs" style="left:509px"><b>2</b>WRITE A DOMAIN NAME</div>
  <div class="ds-step abs" style="left:837px"><b>3</b>WRITE A DOMAIN NAME</div>
</section>

<section class="plans">
  <h2 class="sec-title">MOST POPULAR <span>PLANS</span></h2>
  <p class="sec-lead">Lorem ipsum dolor sit amet, consectetuer adipiscing elit. Suspendisse et justo. Praesent mattis commodo augue. Aliquam ornare hendrerit augue.</p>
  <div class="plan-grid abs">
    <div class="plan"><div class="plan-tab">Basic</div><div class="plan-body"><div class="rate">$9.99 /mo</div><ul><li>1 GB Bandwidth</li><li>256 MB Memory</li><li>24/7 Full Support</li><li>Free Domain Name</li><li>Money back Guarantee</li></ul><span class="signup">Sign Up</span></div></div>
    <div class="plan"><div class="plan-tab">Standard</div><div class="plan-body"><div class="rate">$28.9 /mo</div><ul><li>1 GB Bandwidth</li><li>256 MB Memory</li><li>24/7 Full Support</li><li>Free Domain Name</li><li>Money back Guarantee</li></ul><span class="signup">Sign Up</span></div></div>
    <div class="plan"><div class="plan-tab">Premium</div><div class="plan-body"><div class="rate">$38.9 /mo</div><ul><li>1 GB Bandwidth</li><li>256 MB Memory</li><li>24/7 Full Support</li><li>Free Domain Name</li><li>Money back Guarantee</li></ul><span class="signup">Sign Up</span></div></div>
    <div class="plan"><div class="plan-tab">Unlimited</div><div class="plan-body"><div class="rate">$68.9 /mo</div><ul><li>1 GB Bandwidth</li><li>256 MB Memory</li><li>24/7 Full Support</li><li>Free Domain Name</li><li>Money back Guarantee</li></ul><span class="signup">Sign Up</span></div></div>
  </div>
</section>

<section class="hot-why">
  <div class="hot-col abs"><h2 class="col-title">WHAT'S HOT</h2><div class="col-rule"></div></div>
  <div class="hot-banner abs">
    <div class="server abs" role="img" aria-label="Server tower illustration"></div>
    <div class="badge abs" role="img" aria-label="Price badge"></div>
    <div class="text abs">
      <div class="small">Get up to</div>
      <div class="big"><em>65%</em> OFF ON<br>HOSTING</div>
      <span class="btn-teal more">Read more</span>
    </div>
  </div>
  <div class="dots abs" style="left:332px;top:396px"><i></i><i class="on"></i></div>
  <div class="why-col abs"><h2 class="col-title">WHY QUAY SERVER LANTERN</h2><div class="col-rule"></div></div>
  <div class="why-item abs" style="top:145px"><div class="photo" role="img" aria-label="Hosting hardware photo"></div><div><h4>FAST HOSTING</h4><p>Lorem ipsum dolor sit amet, consectetuer adipiscing elit. Suspendisse et justo. Praesent mattis commodo augue. Aliquam ornare hendrerit augue Cras tellus.</p></div></div>
  <div class="why-item abs" style="top:266px"><div class="photo" role="img" aria-label="Support staff photo"></div><div><h4>WEBSITE PROTECTION</h4><p>Lorem ipsum dolor sit amet, consectetuer adipiscing elit. Suspendisse et justo. Praesent mattis commodo augue. Aliquam ornare hendrerit augue Cras tellus.</p></div></div>
</section>

<section class="voices">
  <div class="abs" style="left:106px;top:60px"><h2 class="col-title">WHAT PEOPLE SAYS</h2><div class="col-rule" style="width:478px;height:2px;background:#ddd"></div></div>
  <div class="quote-box abs">Lorem ipsum dolor sit amet, consectetuer adipiscing elit dolor sit. Suspendisse et justo Praesent mattis commodo augue. Aliquam ornare hendrerit augue Lorem ipsum dolor sit amet, consectetuer</div>
  <div class="author abs"><div class="avatar" role="img" aria-label="Customer portrait"></div><div><div class="name">Ena Marlow</div><div class="role">Marketing - <span>Brevatone</span></div></div></div>
  <div class="dots abs" style="left:332px;top:360px"><i></i><i class="on"></i></div>
  <div class="abs" style="left:628px;top:60px"><h2 class="col-title">GET A <b>WEBSITE</b></h2><div class="col-rule" style="width:472px;height:2px;background:#ddd"></div></div>
  <div class="site-list abs">
    <h4>Create Your Own Website</h4>
    <ul>
      <li><svg viewBox="0 0 12 12"><path d="M1 6l3.5 3.5L11 2" fill="none" stroke="#21b8c1" stroke-width="2"/></svg>Lorem ipsum dolor sit amet sit justo</li>
      <li><svg viewBox="0 0 12 12"><path d="M1 6l3.5 3.5L11 2" fill="none" stroke="#21b8c1" stroke-width="2"/></svg>Nullam turpis. Cras dapibus</li>
      <li><svg viewBox="0 0 12 12"><path d="M1 6l3.5 3.5L11 2" fill="none" stroke="#21b8c1" stroke-width="2"/></svg>Ipsum dolor sit amet sit justo</li>
      <li><svg viewBox="0 0 12 12"><path d="M1 6l3.5 3.5L11 2" fill="none" stroke="#21b8c1" stroke-width="2"/></svg>Lorem ipsum dolor sit amet sit justo</li>
    </ul>
  </div>
  <div class="monitor abs" role="img" aria-label="Desktop computer showing a website"></div>
  <div class="monitor-stand abs"></div>
  <div class="start-badge abs">Start at<br><b>$1.00</b><br>/ mo</div>
</section>

<section class="contact-strip">
  <div class="contact-item abs" style="left:155px"><svg viewBox="0 0 24 24"><path d="M12 2a7 7 0 0 0-7 7c0 5 7 13 7 13s7-8 7-13a7 7 0 0 0-7-7zm0 9.5A2.5 2.5 0 1 1 12 6.5a2.5 2.5 0 0 1 0 5z" fill="#fff"/></svg>Location</div>
  <div class="contact-item abs" style="left:447px"><svg viewBox="0 0 24 24"><rect x="7" y="2" width="10" height="20" rx="2" fill="none" stroke="#fff" stroke-width="2"/><circle cx="12" cy="18" r="1.2" fill="#fff"/></svg>+6541230987</div>
  <div class="contact-item abs" style="left:742px"><svg viewBox="0 0 24 24"><path d="M3 5h13v9H8l-4 3v-3H3z" fill="#fff"/><path d="M18 8h3v9h-1v3l-4-3H9v-1h8V8z" fill="#fff"/></svg>Live Chat</div>
  <div class="contact-item abs" style="left:1034px"><svg viewBox="0 0 24 24"><rect x="2" y="5" width="20" height="14" fill="none" stroke="#fff" stroke-width="2"/><path d="M2 5l10 8 10-8" fill="none" stroke="#fff" stroke-width="2"/></svg>E mail Us</div>
</section>

<footer class="site-footer">
  <div class="foot-col abs" style="left:103px">
    <h4>About Orvane</h4>
    <ul><li>About US</li><li>Contact US</li><li>Hosting Plans</li><li>Affiliates</li><li>Our History</li><li>Tech Support</li><li>My Account</li></ul>
    <div class="news-label">Sign up for special offers</div>
    <div class="news-form"><span class="field">E-Mail Address</span><span class="go">Submit</span></div>
  </div>
  <div class="foot-col abs" style="left:375px">
    <h4>Latest Blog Posts</h4>
    <div class="post"><div class="thumb" role="img" aria-label="Blog post thumbnail"></div><div><div class="t">Suspendisse imperdiet</div><div class="d">Lorem ipsum dolor sit amet</div><div class="m">By Ena Marlow | 15 July</div></div></div>
    <div class="post"><div class="thumb" role="img" aria-label="Blog post thumbnail"></div><div><div class="t">Suspendisse imperdiet</div><div class="d">Lorem ipsum dolor sit amet</div><div class="m">By Ena Marlow | 15 July</div></div></div>
    <div class="post"><div class="thumb" role="img" aria-label="Blog post thumbnail"></div><div><div class="t">Suspendisse imperdiet</div><div class="d">Lorem ipsum dolor sit amet</div><div class="m">By Ena Marlow | 15 July</div></div></div>
  </div>
  <div class="foot-col abs" style="left:647px">
    <h4>Products &amp; Services</h4>
    <ul><li>Website Management</li><li>Domain Services</li><li>Email Services</li><li>E-Commerce Services</li><li>Scripting &amp; Add-ins</li><li>Marketing Services</li><li>E-Commerce Services</li><li>Scripting &amp; Add-ins</li><li>Terms of Service</li><li>Documentation</li></ul>
  </div>
  <div class="foot-col abs" style="left:918px">
    <h4>Legal and Help</h4>
    <ul><li>Contact Us</li><li>Tech Support</li><li>My Account</li><li>Legal</li><li>Privacy</li><li>Report Abuse</li><li>Careers</li><li>Privacy Policy</li><li>Copyright</li><li>Subpoenas</li></ul>
  </div>
</footer>

<section class="copy-bar">
  <p class="abs">Copyright © 2014 | yourdomain.com. All rights reserved.</p>
  <div class="socials abs">
    <span aria-label="Chatterleaf"></span><span aria-label="Murmel"></span><span aria-label="workLoop"></span><span aria-label="Vidplume"></span><span aria-label="Zorbix+"></span><span aria-label="RSS"></span>
  </div>
</section>

</body>
</html>
```